Harlow Ridge & Partners Engineers- WEB DESIGN

I am seeking a more professional face to my current website.

www.HRPengineers.com.au

Using same pages and same text, i need the pages to be presented in a more professional manner.

Use Same logo however all other items may be changed to make it look better... Main theme being a navy blue.

Reason: Alot of recent interest. Awaiting designs.

Target Market(s)

Engineers, Students, Public, Local Authorities, Draftsmen, Architects, Builders etc

Requirements
Must have
• Logo as per site,
• Navy Blue Theme,
• Professional feel,
• Images to attract eye and clients attention. (dont use large infrastructure yet more Residential designs, Crack inspections and Residential Construction)

```html
<!DOCTYPE html>
<html lang="en">
<head>
<meta charset="utf-8">
<title>Harlow Ridge &amp; Partners Engineers</title>
<link rel="stylesheet" href="https://fonts.googleapis.com/css2?family=Open+Sans:ital,wght@0,400;0,600;1,400&display=swap">
<style>
  :root {
    --navy: #2b3a92;
    --navy-dark: #1f2c78;
    --panel: #2f4fa0;
    --sky: #0a84d0;
    --link: #2aa0ea;
    --text: #444444;
    --white: #ffffff;
    --field-border: #c9d0e0;
  }
  * { margin: 0; padding: 0; box-sizing: border-box; }
  html, body { width: 1200px; height: 900px; overflow: hidden; }
  body {
    position: relative;
    background: var(--white);
    font-family: "Open Sans", "Segoe UI", sans-serif;
    color: var(--text);
  }
  .site-header {
    position: absolute; left: 0; top: 0; width: 1200px; height: 147px;
    background: linear-gradient(#f4f4f4, #ffffff 18px);
  }
  .utility-links {
    position: absolute; right: 102px; top: 7px;
    font-size: 14px; font-style: italic; color: #333;
  }
  .brand {
    position: absolute; left: 0; width: 1200px; top: 74px;
    display: flex; justify-content: center; align-items: center; gap: 12px;
  }
  .brand-mark { width: 18px; height: 18px; background: var(--navy); }
  .brand-name {
    font-size: 24px; font-weight: 600; color: var(--navy); letter-spacing: 0.5px;
  }
  .main-nav {
    position: absolute; left: 0; top: 147px; width: 1200px; height: 43px;
    background: var(--navy);
  }
  .main-nav a {
    position: absolute; top: 14px; font-size: 14px; color: var(--white);
    text-decoration: none; text-transform: uppercase;
  }
  .hero {
    position: absolute; left: 0; top: 190px; width: 1200px; height: 478px;
    background:
      radial-gradient(ellipse 500px 180px at 950px 420px, rgba(230,150,60,0.45), transparent 70%),
      radial-gradient(ellipse 260px 140px at 60px 420px, rgba(220,140,60,0.4), transparent 70%),
      linear-gradient(#0d2a6e 0%, #163a82 45%, #10224a 75%, #0b1428 100%);
  }
  .hero-caption {
    position: absolute; left: 101px; top: 375px; width: 493px; height: 171px;
    background: rgba(10, 20, 35, 0.72);
    padding: 18px 0 0 15px; color: var(--white);
  }
  .hero-caption h1 {
    font-size: 39px; font-weight: 400; line-height: 49px;
  }
  .hero-caption p { font-size: 19px; margin-top: 3px; margin-left: 3px; }
  .hero-caption em { font-style: normal; color: var(--link); }
  .slider-dots { position: absolute; left: 1033px; top: 600px; display: flex; gap: 5px; }
  .slider-dots span { width: 12px; height: 12px; border-radius: 50%; background: var(--white); }
  .slider-dots span.active { background: var(--sky); border: 2px solid var(--white); }
  .accent-band {
    position: absolute; left: 0; top: 668px; width: 1200px; height: 12px; background: var(--sky);
  }
  .section-title {
    position: absolute; left: 101px; top: 640px; width: 632px; height: 40px;
    background: var(--sky); color: var(--white);
    font-size: 19px; padding: 9px 0 0 14px; text-transform: uppercase;
  }
  .intro {
    position: absolute; left: 103px; top: 695px; width: 620px;
    font-size: 15px; line-height: 20px; color: var(--text);
  }
  .intro p { margin-bottom: 20px; }
  .register-panel {
    position: absolute; left: 733px; top: 622px; width: 367px; height: 278px;
    background: var(--panel);
  }
  .register-panel h2 {
    position: absolute; left: 29px; top: 20px;
    font-size: 21px; font-weight: 400; color: var(--white);
  }
  .field {
    position: absolute; left: 24px; width: 319px; height: 33px;
    background: var(--white); border: 2px solid var(--field-border);
    font-size: 15px; font-style: italic; color: #8a8a8a; padding: 5px 0 0 9px;
  }
  .select-arrow {
    position: absolute; right: 8px; top: 7px; width: 17px; height: 16px;
    border: 1px solid #555; background: #eee;
  }
  .social-rail {
    position: absolute; left: 1150px; top: 785px; width: 50px; height: 105px;
    background: var(--white); border: 1px solid #ccc; border-right: none;
  }
  .social-rail span {
    position: absolute; left: 8px; width: 33px; height: 33px; border-radius: 50%;
  }
</style>
</head>
<body>
  <header class="site-header">
    <div class="utility-links">Register Now | Contact Us</div>
    <div class="brand">
      <span class="brand-mark"></span>
      <span class="brand-name">Harlow Ridge &amp; Partners Engineers</span>
    </div>
  </header>

  <nav class="main-nav">
    <a href="#" style="left:112px">Home</a>
    <a href="#" style="left:184px">Structural Engineering</a>
    <a href="#" style="left:400px">Energy Rating</a>
    <a href="#" style="left:544px">House Inspections</a>
    <a href="#" style="left:724px">Construction</a>
    <a href="#" style="left:868px">Register Now</a>
    <a href="#" style="left:1003px">Contact Us</a>
  </nav>

  <div class="hero" role="img" aria-label="Night photograph of a city riverbank with lit towers and waterfront promenade"></div>
  <div class="hero-caption">
    <h1>Harlow Ridge &amp; Partners<br>Engineers</h1>
    <p>can help you with all your <em>Building</em> requirements.</p>
  </div>
  <div class="slider-dots"><span class="active"></span><span></span><span></span><span></span></div>

  <div class="accent-band"></div>
  <h2 class="section-title">Structural Engineers Melbourne</h2>

  <section class="intro">
    <p>Melbourne based Structural Engineers Design, Site Inspections, Crack Inspections, Inspection Reports, 6 Star Energy Ratings, Certificate of Compliance Form 1507, Harlow Ridge &amp; Partners Engineers can help you with all your building requirements.</p>
    <p>Your project is our product and as such we pride ourselves to deliver it with ease to you at only the highest standards in quality &amp; design.</p>
    <p>Catering for all facets of Residential Planning, Design &amp; Construction, HRP Engineers can help every step of the way.</p>
    <p>As Harlow Ridge &amp; Partners Engineers we will work closely with you to ensure the best result for every client.</p>
  </section>

  <aside class="register-panel">
    <h2>REGISTER</h2>
    <div class="field" style="top:64px">Business Name</div>
    <div class="field" style="top:107px">Suburb</div>
    <div class="field" style="top:150px">State
      <svg class="select-arrow" viewBox="0 0 17 16"><path d="M5 6 L12 6 L8.5 11 Z" fill="#333"/></svg>
    </div>
    <div class="field" style="top:194px">Your Name</div>
    <div class="field" style="top:237px">Your Phone</div>
  </aside>

  <div class="social-rail">
    <span style="top:15px; background:#3b5998"></span>
    <span style="top:59px; background:#d34836"></span>
  </div>
</body>
</html>
```